Web Infographic Series

We need a series of 4 infographics to highlight the major findings of a recent report our company published called the "Whole Staff Transit Comparison Study".

We plan to use these infographics on web pages, in social media, and other channels to promote the survey and generate interest in what our company does.

The phrase "Whole Staff Transit" is a registered tradfemark of Felkovar Worldwide, so we actually mark it with the (R). We have a tight timeline but WE KNOW YOU CAN DO IT! We have thrown together rough mock ups of the information we want and some of the images that we need to comply with our brand standard to help you.

A overview document of what we want to communicate in the graphics is attached!!
Updates

Please see updated brief!  It will give you the data points and info you need to get started.  Thanks!

Target Market(s)

WE are a B2B company and our target audience is finance executives, HR executives and purchasing/procurement executives. visit www.felkovar-example.com to get a sense of our "look and feel".

Industry/Entity Type

It Company

Requirements
Must have
• The Felkovar Worldwide "80th anniversary logo", a (R) after the first mention of the phrase "Whole Staff Transit", Color scheme of red gradient to dark red with gray, white and accent colors or images (i.e. R 169 G 31 B 35 to a dark red 80 22 16) Must be high impact and fit in with the style of the graphics we have done before see some examples on https://www.felkovar-example.com/Solutions/Business-Vehicle-Services/Compare-Your-Business-Vehicle-Program-Options.aspx .. and the cover of the report.....we are open to new interpretations of improvements of course!
Nice to have
• we have a set of "mobility" icons attached below. we would like to see them incorporated in the design as well as an image of the cover of the report.
Should not have
• A dark (black) color scheme. Too much color. a cartoon-ish look

```html
<!DOCTYPE html>
<html lang="en">
<head>
<meta charset="utf-8">
<title>Whole Staff Transit – Overall Key Findings</title>
<link href="https://fonts.googleapis.com/css2?family=Open+Sans:wght@400;600;700&display=swap" rel="stylesheet">
<style>
:root{
  --red:#a91f23;
  --red-dark:#501610;
  --red-mid:#8a1a1d;
  --red-chart:#7a1619;
  --grey:#e6e6e6;
  --grey-text:#555;
  --blue:#1f74bf;
  --orange:#f5a623;
  --white:#ffffff;
}
*{margin:0;padding:0;box-sizing:border-box}
html,body{width:1200px;height:4027px;overflow:hidden;background:var(--white)}
body{font-family:"Open Sans",Arial,sans-serif;position:relative}
.section{position:absolute;left:0;width:1200px}
.header{top:0;height:545px;background:linear-gradient(160deg,var(--red) 0%,var(--red-dark) 100%)}
.badge{position:absolute;left:488px;top:10px;width:224px;height:224px;border-radius:50%;background:var(--white);border:10px solid var(--red-mid);display:flex;align-items:center;justify-content:center;text-align:center}
.badge-name{font-size:30px;font-weight:700;color:var(--red);line-height:1.1}
.title{position:absolute;top:300px;left:0;width:1200px;text-align:center;color:var(--white);font-size:58px;font-weight:600;line-height:1.2}
.title sup{font-size:36px}
.overview{top:545px;height:485px;background:var(--grey)}
.donut{position:absolute;left:60px;top:0px}
.stat-mobile{position:absolute;left:800px;top:100px;width:380px;color:var(--grey-text);font-size:30px;line-height:1.25}
.stat-mobile strong{color:var(--red);font-size:54px;font-weight:700}
.stat-nonmobile{position:absolute;left:820px;top:330px;color:var(--blue);font-size:44px}
.stat-nonmobile strong{font-weight:700;font-size:54px}
.icon-car{position:absolute}
.productivity{top:1030px;height:1630px;background:linear-gradient(180deg,var(--red) 0%,var(--red-mid) 100%)}
.notch{position:absolute}
.lead{position:absolute;left:140px;top:175px;width:950px;color:var(--white);font-size:26px;font-weight:700;line-height:1.35}
.big-stat{position:absolute;left:180px;top:320px;color:var(--white);font-size:72px;line-height:1.1;text-align:center}
.big-stat strong{font-size:100px;font-weight:400;display:block}
.ring{position:absolute;left:700px;top:250px}
.legend{position:absolute;top:725px;color:var(--white);font-size:30px;display:flex;align-items:center;gap:22px}
.legend .dot{width:46px;height:46px;border-radius:50%;border:4px solid var(--white)}
.chart{position:absolute;top:800px;left:0;width:1200px;height:800px}
.growth{top:2660px;height:565px;background:var(--white)}
.growth-title{position:absolute;top:70px;left:0;width:1200px;text-align:center;color:var(--red);font-size:60px;font-weight:400}
.growth-art{position:absolute;left:60px;top:210px;width:440px;height:320px;background:linear-gradient(135deg,#c9373b,#7a1619);border-radius:12px}
.growth-text{position:absolute;left:560px;top:260px;width:600px;color:var(--grey-text);font-size:38px;line-height:1.3}
.spend{top:3225px;height:645px;background:linear-gradient(180deg,var(--red) 0%,var(--red-dark) 100%)}
.spend-title{position:absolute;top:60px;left:60px;width:1080px;text-align:center;color:var(--white);font-size:52px;line-height:1.2}
.houses{position:absolute;left:0;top:0}
.spend-note{position:absolute;width:380px;text-align:center;color:var(--white);font-size:30px;line-height:1.3;font-style:italic}
.spend-note.high{left:110px;top:290px}
.spend-note.low{left:720px;top:290px}
.footer{top:3870px;height:157px;background:var(--white);display:flex;align-items:center;justify-content:center;gap:18px}
.footer .mark{width:44px;height:44px;background:var(--red)}
.footer .name{font-size:48px;font-weight:700;color:var(--red)}
</style>
</head>
<body>

<section class="section header">
  <div class="badge"><span class="badge-name">Felkovar<br>Worldwide</span></div>
  <h1 class="title">Whole Staff Transit<sup> ®</sup><br>Overall Key Findings:</h1>
</section>

<section class="section overview">
  <svg class="donut" width="560" height="485" viewBox="0 0 560 485">
    <circle cx="240" cy="220" r="185" fill="none" stroke="#1f74bf" stroke-width="75"/>
    <circle cx="240" cy="220" r="185" fill="none" stroke="#a91f23" stroke-width="75"
      stroke-dasharray="348.7 813.6" transform="rotate(-90 240 220)"/>
  </svg>
  <p class="stat-mobile"><strong>30%</strong> of the workforce is mobile - which means they travel, drive vehicles, or relocate for business</p>
  <svg class="icon-car" style="left:1090px;top:240px" width="90" height="50" viewBox="0 0 90 50">
    <path d="M8 34 L14 20 Q18 12 28 12 L58 12 Q66 12 72 20 L82 28 Q88 30 88 36 L88 40 L2 40 L2 36 Z" fill="#a91f23"/>
    <circle cx="22" cy="40" r="8" fill="#501610"/><circle cx="68" cy="40" r="8" fill="#501610"/>
  </svg>
  <p class="stat-nonmobile"><strong>70%</strong> non-mobile</p>
  <svg class="icon-car" style="left:860px;top:420px" width="110" height="60" viewBox="0 0 110 60">
    <path d="M18 38 L24 24 Q28 16 38 16 L68 16 Q76 16 82 24 L92 32 Q98 34 98 40 L98 44 L12 44 L12 40 Z" fill="#1f74bf"/>
    <circle cx="32" cy="44" r="8" fill="#1f74bf"/><circle cx="78" cy="44" r="8" fill="#1f74bf"/>
    <path d="M10 8 L100 56 M100 8 L10 56" stroke="#444" stroke-width="5"/>
  </svg>
</section>

<section class="section productivity">
  <svg class="notch" style="left:920px;top:0" width="120" height="60" viewBox="0 0 120 60">
    <polygon points="0,0 120,0 60,60" fill="#e6e6e6"/>
  </svg>
  <p class="lead">Companies with mobility programs have higher productivity. An average of 85% reported that they saw improved employee productivity after implementing a defined mobility program.</p>
  <p class="big-stat"><strong>85%</strong>employee<br>productivity</p>
  <svg class="ring" width="460" height="460" viewBox="0 0 460 460">
    <polygon points="0,230 60,200 60,260" fill="#ffffff"/>
    <circle cx="240" cy="230" r="150" fill="none" stroke="#ffffff" stroke-width="90"
      stroke-dasharray="801 942.5" transform="rotate(-60 240 230)"/>
  </svg>
  <div class="legend" style="left:170px"><span class="dot" style="background:var(--blue)"></span>Residents who implemented it</div>
  <div class="legend" style="left:660px"><span class="dot" style="background:var(--orange)"></span>Residents Reporting Improved Productivity</div>

  <svg class="chart" viewBox="0 0 1200 800">
    <rect x="0" y="0" width="1200" height="590" fill="#7a1619" opacity="0.45"/>
    <g stroke="#ffffff" stroke-width="2" opacity="0.35">
      <line x1="90" y1="0" x2="90" y2="590"/><line x1="282" y1="0" x2="282" y2="590"/>
      <line x1="475" y1="0" x2="475" y2="590"/><line x1="665" y1="0" x2="665" y2="590"/>
      <line x1="870" y1="0" x2="870" y2="590"/><line x1="1055" y1="0" x2="1055" y2="590"/>
    </g>
    <polyline points="0,135 90,125 282,105 475,32 665,85 870,105 1055,65 1200,45" fill="none" stroke="#f5a623" stroke-width="6"/>
    <polyline points="0,560 90,548 282,520 475,500 665,488 870,447 1055,427 1200,400" fill="none" stroke="#1f74bf" stroke-width="6"/>
    <g font-family="Open Sans, Arial, sans-serif" font-size="28" fill="#f5a623" text-anchor="middle">
      <text x="90" y="95">81%</text><text x="282" y="75">83%</text><text x="475" y="20">96%</text>
      <text x="665" y="55">87%</text><text x="870" y="75">82%</text><text x="1055" y="45">87%</text>
    </g>
    <g font-family="Open Sans, Arial, sans-serif" font-size="28" fill="#4a9ae0" text-anchor="middle">
      <text x="90" y="520">21%</text><text x="282" y="492">23%</text><text x="475" y="472">25%</text>
      <text x="665" y="460">30%</text><text x="870" y="420">48%</text><text x="1055" y="400">54%</text>
    </g>
    <g font-family="Open Sans, Arial, sans-serif" font-size="20" fill="#ffffff" text-anchor="middle">
      <text x="90" y="630">company</text><text x="90" y="654">vehicles</text>
      <text x="282" y="630">relocation</text><text x="282" y="654">program</text>
      <text x="475" y="630">expenses mgmt</text><text x="475" y="654">software</text>
      <text x="665" y="630">tools/software/</text><text x="665" y="654">apps for mobile</text>
      <text x="870" y="630">personal vehicle</text><text x="870" y="654">reimbursement program</text>
      <text x="1055" y="630">mobile</text><text x="1055" y="654">devices</text>
    </g>
    <g fill="#ffffff">
      <path d="M62 710 L68 696 Q72 690 80 690 L100 690 Q108 690 112 696 L120 704 L120 714 L60 714 Z"/>
      <circle cx="74" cy="716" r="6"/><circle cx="106" cy="716" r="6"/>
      <rect x="262" y="690" width="40" height="30" fill="none" stroke="#fff" stroke-width="5"/>
      <path d="M270 705 L294 705 M286 697 L294 705 L286 713" stroke="#fff" stroke-width="4" fill="none"/>
      <circle cx="475" cy="705" r="14"/>
      <g stroke="#fff" stroke-width="7"><line x1="475" y1="683" x2="475" y2="727"/><line x1="453" y1="705" x2="497" y2="705"/><line x1="459" y1="689" x2="491" y2="721"/><line x1="491" y1="689" x2="459" y2="721"/></g>
      <circle cx="475" cy="705" r="6" fill="#8a1a1d"/>
      <path d="M645 720 L670 695 L680 705 L655 730 Z"/><circle cx="683" cy="690" r="9"/>
      <path d="M842 710 L848 696 Q852 690 860 690 L880 690 Q888 690 892 696 L900 704 L900 714 L840 714 Z"/>
      <circle cx="854" cy="716" r="6"/><circle cx="886" cy="716" r="6"/>
      <rect x="1040" y="684" width="30" height="46" rx="5" fill="none" stroke="#fff" stroke-width="5"/>
    </g>
  </svg>
  <svg class="notch" style="left:920px;top:1630px" width="120" height="50" viewBox="0 0 120 50"></svg>
</section>

<section class="section growth">
  <svg class="notch" style="left:920px;top:0" width="120" height="50" viewBox="0 0 120 50">
    <polygon points="0,0 120,0 60,50" fill="#8a1a1d"/>
  </svg>
  <h2 class="growth-title">Growing organizations are investing in mobility</h2>
  <div class="growth-art" role="img" aria-label="Illustration of a red car with stacked red cubes and a dollar price tag"></div>
  <p class="growth-text">Companies with 10% or more annual growth in revenue have more mobile employees than companies with low growth.</p>
</section>

<section class="section spend">
  <svg class="notch" style="left:920px;top:0" width="120" height="50" viewBox="0 0 120 50">
    <polygon points="0,0 120,0 60,50" fill="#ffffff"/>
  </svg>
  <h2 class="spend-title">Mobility differences between high-growth and low-growth companies</h2>
  <svg class="houses" width="1200" height="645" viewBox="0 0 1200 645">
    <polygon points="60,645 60,520 300,470 540,520 540,645" fill="#ffffff"/>
    <polygon points="660,645 660,520 900,470 1140,520 1140,645" fill="#ffffff"/>
  </svg>
  <p class="spend-note high">growth organizations invest average of $11,779/mobile employee</p>
  <p class="spend-note low">non-growth organizations only invest an average of $6,527/mobile employee</p>
</section>

<footer class="section footer">
  <span class="mark"></span><span class="name">Felkovar Worldwide</span>
</footer>

</body>
</html>
```